Consulting Company Business Card

I am looking for a minimalist, classy, professional design on my business card. I would like it to be double-sided. I want to use the font and color scheme of my logo which are attached. Please be creative in the designs that you send me. I want to play off the design of my logo with the inner C that is Green and Blue broken up with the white.
Target Market(s)
Small Businesses
Industry/Entity Type
Consulting
Contact Information for Business Card
Derek L. Whitmore, CPA CGMA, 555-014-2283, dwhitmore@brovantadvisory.example, www.brovantadvisory.example

```html
<!DOCTYPE html>
<html lang="en">
<head>
<meta charset="utf-8">
<title>Brovant Advisory – Business Card</title>
<link href="https://fonts.googleapis.com/css2?family=Montserrat:wght@400;500;700&display=swap" rel="stylesheet">
<style>
  :root {
    --navy: #283462;
    --teal: #3ba59b;
    --ink: #2b2d33;
    --paper: #ffffff;
    --stage: #eceef1;
    --shadow: rgba(30, 36, 60, 0.16);
  }
  * { box-sizing: border-box; margin: 0; padding: 0; }
  html, body {
    width: 809px;
    height: 1200px;
    overflow: hidden;
    background: var(--stage);
    font-family: "Montserrat", Arial, sans-serif;
  }
  .sheet {
    width: 809px;
    height: 1200px;
    display: flex;
    flex-direction: column;
    align-items: center;
    justify-content: center;
    gap: 90px;
  }
  .card {
    position: relative;
    width: 620px;
    height: 354px;
    background: var(--paper);
    box-shadow: 0 14px 34px var(--shadow);
    overflow: hidden;
  }

  /* Front: brand side */
  .card--front {
    display: flex;
    align-items: center;
    justify-content: center;
  }
  .brand {
    display: flex;
    align-items: center;
    gap: 16px;
  }
  .brand__dot {
    width: 30px;
    height: 30px;
    border-radius: 50%;
    background: var(--teal);
  }
  .brand__name {
    font-weight: 700;
    font-size: 34px;
    letter-spacing: 1px;
    color: var(--navy);
    text-transform: uppercase;
  }

  /* Back: contact side */
  .card--back { padding: 0; }
  .accent-bar {
    position: absolute;
    left: 44px;
    top: 0;
    width: 14px;
    height: 172px;
    background: var(--navy);
  }
  .contact {
    position: absolute;
    left: 78px;
    top: 112px;
  }
  .contact__name {
    font-weight: 700;
    font-size: 25px;
    color: var(--ink);
  }
  .contact__title {
    margin-top: 4px;
    font-weight: 500;
    font-size: 15px;
    letter-spacing: 0.5px;
    color: var(--teal);
  }
  .contact__list {
    list-style: none;
    margin-top: 34px;
    display: flex;
    flex-direction: column;
    gap: 11px;
  }
  .contact__item {
    display: flex;
    align-items: center;
    gap: 12px;
    font-size: 14px;
    color: var(--ink);
  }
  .contact__icon {
    width: 18px;
    height: 18px;
    flex: none;
  }
</style>
</head>
<body>
  <main class="sheet">
    <section class="card card--front" aria-label="Card front">
      <div class="brand">
        <span class="brand__dot"></span>
        <span class="brand__name">Brovant Advisory</span>
      </div>
    </section>

    <section class="card card--back" aria-label="Card back">
      <span class="accent-bar"></span>
      <div class="contact">
        <h1 class="contact__name">Derek L. Whitmore</h1>
        <p class="contact__title">CPA CGMA</p>
        <ul class="contact__list">
          <li class="contact__item">
            <svg class="contact__icon" viewBox="0 0 18 18" aria-hidden="true">
              <circle cx="9" cy="9" r="9" fill="#283462"/>
              <path d="M6.2 4.6l1.4 1.9-.8 1.1c.6 1.3 1.5 2.2 2.8 2.8l1.1-.8 1.9 1.4-.7 1.6c-3.6-.3-6.7-3.4-7-7z" fill="#fff"/>
            </svg>
            555-014-2283
          </li>
          <li class="contact__item">
            <svg class="contact__icon" viewBox="0 0 18 18" aria-hidden="true">
              <circle cx="9" cy="9" r="9" fill="#283462"/>
              <rect x="4.5" y="5.8" width="9" height="6.4" rx="0.6" fill="#fff"/>
              <path d="M4.8 6.2L9 9.4l4.2-3.2" fill="none" stroke="#283462" stroke-width="0.9"/>
            </svg>
            dwhitmore@brovantadvisory.example
          </li>
          <li class="contact__item">
            <svg class="contact__icon" viewBox="0 0 18 18" aria-hidden="true">
              <circle cx="9" cy="9" r="9" fill="#283462"/>
              <g fill="none" stroke="#fff" stroke-width="0.9">
                <circle cx="9" cy="9" r="4.4"/>
                <ellipse cx="9" cy="9" rx="1.9" ry="4.4"/>
                <path d="M4.6 9h8.8"/>
              </g>
            </svg>
            www.brovantadvisory.example
          </li>
        </ul>
      </div>
    </section>
  </main>
</body>
</html>
```